Forking Well Buisiness card

needing a Business card for our company - Forking Well.
Forking well is co owned by Jess and Owen Marchetti (Husband and Wife)
Services Forking Well provides include:
Dietetic/nutrition Consultations, weight loss coaching programs, personal and group training, post injury rehab, health and nutrition presentations and Health Retreats.
Jess:
Accredited Practicing Dietitian & Personal trainer
Owen:
Personal trainer, rehab trainer & Strength and conditioning coach
At this stage the business cards will be made just for Jess.
She has a training studio in Armadale and Dietetics private practice in Richmond.
Mobile services are also available (i.e. meet at house or local cafe)

We need the card to look smart, modern and combine both nutrition and training.
We already have a logo which I will attach.
I was initial thinking i black background but am open to suggestions.

Target Market(s)

Health concious, People with money,

Industry/Entity Type

Nutrition

Contact Information for Business Card

Forking Well
Jess Marchetti
M: 0417390265
E: forkingwell@mailnest.com
W: www.forkingwell.com.au
Address:
Dietetics: Level 1, 583 Bellow Street
Richmond VIC 3121
Training: Private Studio, behind 2087 Tamsin St
ARMADALE, VIC, 3143

Requirements
Must have
• Must have logo (see attached) please not the one we use is the top left (blue and green)
please note attachment is top left (green and blue)

needs to be clear to read - the font needs to be clear and sharp and the background cannot be too busy.eg funny patterns.
Could I please see a card with a line for 'appointment time/date:' possibly on the back. Would like to see what this looks like.
Jess Marchetti's Profile (side of card) must include "Accredited Practicing Dietitian" and "Personal Trainer."
I like when the services forking well provide are in dot form.
Nice to have
• would like the card to be 2 sides
first side:
Forking well logo - Large
services forking well provides: Dietetic/nutrition Consultations, weight loss coaching programs, personal and group training, post injury rehab, health and nutrition presentations and Health Retreats.
web address
second side:
smaller logo
Details for Jess:
Accredited Practicing Dietitian
Personal Trainer
Contact Details:
M: 0417390265
E: forkingwell@mailnest.com
Address:
Richmond VIC 3121
ARMADALE, VIC, 3143
Should not have
• Dietetic + nutrition consultations
Should say dietetic/nutrition consultations (first letter of words in capitals please)
Please write phone number as 0417 390 265
Not: 04 17 390265
- note numbers as 4, 3, 3.

```html
<!DOCTYPE html>
<html lang="en">
<head>
<meta charset="utf-8">
<title>Forking Well Business Card</title>
<link rel="stylesheet" href="https://fonts.googleapis.com/css2?family=Anton&family=Arimo:wght@400;700&display=swap">
<style>
  :root {
    --stage-light: #b9b9b9;
    --stage-dark: #7e7e7e;
    --card-black: #151515;
    --card-black-glow: #3a3a3a;
    --accent-green: #8cd23c;
    --accent-blue: #1a5fc4;
    --front-green: #8cc63f;
    --front-teal: #3f8f7a;
    --front-blue: #0b55a8;
    --front-pale: #d8f0b0;
    --logo-ink: #333333;
    --text-white: #ffffff;
    --text-soft: #e6e6e6;
  }
  * { margin: 0; padding: 0; box-sizing: border-box; }
  html, body { width: 1200px; height: 727px; overflow: hidden; }
  body {
    background: radial-gradient(ellipse at 50% 35%, var(--stage-light), var(--stage-dark));
    font-family: "Arimo", Arial, sans-serif;
    position: relative;
  }
  .card {
    position: absolute;
    top: 211px;
    width: 530px;
    height: 305px;
    overflow: hidden;
    box-shadow: 0 14px 30px rgba(0,0,0,.35);
  }
  /* Profile side */
  .card-profile {
    left: 45px;
    background: radial-gradient(ellipse at 45% 35%, var(--card-black-glow), var(--card-black) 70%);
  }
  .card-profile .swooshes { position: absolute; inset: 0; }
  .small-logo {
    position: absolute;
    top: 40px; left: 0; right: 0;
    display: flex; align-items: center; justify-content: center; gap: 8px;
    font-size: 22px; color: var(--accent-blue);
  }
  .small-logo .mark {
    width: 14px; height: 14px; border-radius: 50%;
    background: var(--accent-green);
  }
  .profile {
    position: absolute; left: 34px; top: 150px;
    color: var(--text-white);
  }
  .profile-name {
    font-family: "Anton", Impact, sans-serif;
    font-size: 22px; color: var(--accent-green); letter-spacing: .3px;
    margin-bottom: 6px;
  }
  .profile-role { font-size: 17px; line-height: 1.3; letter-spacing: .6px; }
  .contacts {
    position: absolute; left: 292px; top: 96px; width: 228px;
    color: var(--accent-green); font-size: 10px; line-height: 1.45;
  }
  .contacts-title { font-size: 14px; margin-bottom: 8px; }
  .contacts p + p.gap { margin-top: 8px; }

  /* Services side */
  .card-services {
    left: 625px;
    background: linear-gradient(35deg, var(--front-pale) 0%, var(--front-green) 28%, var(--front-teal) 60%, var(--front-blue) 100%);
  }
  .big-logo {
    position: absolute; left: 28px; top: 200px;
    display: flex; align-items: center; gap: 10px;
    font-size: 34px; color: var(--logo-ink); letter-spacing: -.5px;
  }
  .big-logo .mark {
    width: 24px; height: 24px; border-radius: 50%;
    background: var(--logo-ink);
  }
  .services {
    position: absolute; left: 272px; top: 40px; width: 240px;
    color: var(--text-white);
  }
  .services-title {
    font-family: "Anton", Impact, sans-serif;
    font-size: 21px; line-height: 1.1; margin-bottom: 8px;
  }
  .services-list { font-size: 12.5px; line-height: 1.35; color: var(--text-soft); }
  .services-web {
    font-family: "Anton", Impact, sans-serif;
    font-size: 15px; margin-top: 26px; text-align: center;
  }
</style>
</head>
<body>

<section class="card card-profile" aria-label="Business card, profile side">
  <svg class="swooshes" viewBox="0 0 530 305" preserveAspectRatio="none" aria-hidden="true">
    <path d="M300 0 Q430 20 530 70 L530 58 Q440 10 340 0 Z" fill="var(--accent-green)"/>
    <path d="M0 235 Q120 300 330 305 L250 305 Q100 295 0 250 Z" fill="var(--accent-blue)"/>
  </svg>
  <div class="small-logo"><span class="mark"></span><span>Forking Well</span></div>
  <div class="profile">
    <h1 class="profile-name">Jess Marchetti</h1>
    <p class="profile-role">Accredited practicing dietitian</p>
    <p class="profile-role">Personal trainer</p>
  </div>
  <div class="contacts">
    <p class="contacts-title">Contact Details:</p>
    <p>M: 0417 390 265</p>
    <p>E: forkingwell@mailnest.com</p>
    <p class="gap">Dietetics: Level 1, 583 Bellow Street</p>
    <p>Richmond VIC 3121</p>
    <p>Training: Private Studio, behind 2087 Tamsin St</p>
    <p>ARMADALE, VIC, 3143</p>
  </div>
</section>

<section class="card card-services" aria-label="Business card, services side">
  <div class="big-logo"><span class="mark"></span><span>Forking Well</span></div>
  <div class="services">
    <h2 class="services-title">Services Forking Well provides:</h2>
    <p class="services-list">dietetic/nutrition consultations, weight loss coaching programs, personal and group training, post injury rehab, health and nutrition presentations and health retreats.</p>
    <p class="services-web">www.forkingwell.com.au</p>
  </div>
</section>

</body>
</html>
```